New candle on the block - the market is saturated and I’m starting a company!! What?!?

Hello,
I am looking for a label design for my candles. I would love to have a blonde silhouette with a bow of some sort in her hair. My future labels will have the bow changing color or design based on the candle. Example a strawberry scented candle will have a girl with strawberry's pictured on the bow, my unicorn candles will have a multicolor bow.
I'm not against the vertical label and im not against a horizontal label. This will also be going on my bath bomb boxes and bath milks and salts bottles. My product is all high quality ingrediencies, Organic and natural only.
I'n my mind I imagine the font for " Velvet Marigold" as a really pretty cursive and sort of rose gold but I'm also pretty terrible at design. Please feel free to ask questions and take a creative liberty. I've added photos of what the vessels will most likely look like. It would be girly and along these lines as well as one of the boxes I plan to ship candles in.

Thanks!

Target Market(s)

People seeking clean burning candles and organic bath products

Industry/Entity Type

Bath and beauty

Requirements
Must have
• Girl with a bow in hair. She can be any color just as long as the bow stands out as a different color
Nice to have
• Clean, sophisticated, girly. Maybe rose gold and coordinating tones?
Should not have
• Busy, wild designs or colors.

```html
<!DOCTYPE html>
<html lang="en">
<head>
<meta charset="utf-8">
<title>Velvet Marigold – Candle Labels</title>
<link rel="stylesheet" href="https://fonts.googleapis.com/css2?family=Josefin+Sans:wght@400&family=Cormorant+Garamond:wght@400&display=swap">
<style>
  :root {
    --backdrop: #a7bcbd;
    --label-paper: #f4f4f2;
    --ink: #111111;
    --frame: #1a1a1a;
    --bow-red-light: #e24a3b;
    --bow-red-dark: #b5160f;
    --bow-multi-a: #3aa8d8;
    --bow-multi-b: #7cc043;
    --bow-multi-c: #f2c230;
    --hair-grey: #8a8a8a;
    --hair-light: #d8d8d8;
  }
  * { box-sizing: border-box; margin: 0; padding: 0; }
  html, body {
    width: 1200px;
    height: 900px;
    overflow: hidden;
    background: var(--backdrop);
  }
  .label-sheet {
    width: 1200px;
    height: 900px;
    display: flex;
    align-items: center;
    justify-content: center;
    gap: 80px;
  }
  .candle-label {
    width: 460px;
    height: 460px;
    background: var(--label-paper);
    padding: 22px;
    box-shadow: 0 6px 18px rgba(40, 60, 60, 0.18);
  }
  .label-frame {
    width: 100%;
    height: 100%;
    border: 2px solid var(--frame);
    display: flex;
    flex-direction: column;
    align-items: center;
    padding-top: 34px;
  }
  .label-illustration {
    width: 150px;
    height: 160px;
    border-radius: 6px;
  }
  .label-illustration--strawberry {
    background: linear-gradient(180deg, var(--bow-red-light) 0%, var(--bow-red-dark) 28%, var(--hair-grey) 30%, var(--hair-light) 100%);
  }
  .label-illustration--unicorn {
    background: linear-gradient(180deg, var(--bow-multi-a) 0%, var(--bow-multi-b) 14%, var(--bow-multi-c) 28%, var(--hair-grey) 30%, var(--hair-light) 100%);
  }
  .brand-name {
    margin-top: 26px;
    font-family: "Josefin Sans", sans-serif;
    font-weight: 400;
    font-size: 40px;
    letter-spacing: 1px;
    color: var(--ink);
    text-transform: uppercase;
    line-height: 1;
  }
  .scent-name {
    margin-top: 22px;
    font-family: "Cormorant Garamond", serif;
    font-size: 19px;
    color: var(--ink);
  }
  .net-weight {
    margin-top: 18px;
    font-family: "Cormorant Garamond", serif;
    font-size: 15px;
    color: var(--ink);
  }
</style>
</head>
<body>
  <main class="label-sheet">
    <section class="candle-label">
      <div class="label-frame">
        <div class="label-illustration label-illustration--strawberry" role="img" aria-label="Line illustration of a woman's head with hair in a messy bun tied with a red bow"></div>
        <h1 class="brand-name">Velvet Marigold</h1>
        <p class="scent-name">Strawberry Scented</p>
        <p class="net-weight">10.5 oz (300 g)</p>
      </div>
    </section>
    <section class="candle-label">
      <div class="label-frame">
        <div class="label-illustration label-illustration--unicorn" role="img" aria-label="Line illustration of a woman's head with hair in a messy bun tied with a multicolour bow"></div>
        <h2 class="brand-name">Velvet Marigold</h2>
        <p class="scent-name">Unicorn Candles</p>
        <p class="net-weight">10.5 oz (300 g)</p>
      </div>
    </section>
  </main>
</body>
</html>
```